Candy gift box

I want a fun design like the attachments with my company name on it. I want to use this box to hold small plastic 2x2x2 containers of candy. So I need this box to be the wow factor and something unique. Box size is 10.125x6.5x2.75. I would also like it to have maybe a few fun words and even a dots on top would also like to fun bright colour for inside the flap. Company name is Tartwhirl.

• Bright fun colours even dots or confetti

```html
<!DOCTYPE html>
<html lang="en">
<head>
<meta charset="utf-8">
<title>Tartwhirl Candy Gift Box Dieline</title>
<link href="https://fonts.googleapis.com/css2?family=Tinos:wght@700&display=swap" rel="stylesheet">
<style>
  :root {
    --berry: #b21e65;
    --candy-pink: #e66fa2;
    --mint: #89cca5;
    --white: #ffffff;
    --confetti-warm: #f7b36a;
    --confetti-cool: #5aaede;
    --confetti-violet: #8e3c97;
  }
  html, body {
    margin: 0;
    padding: 0;
    width: 1200px;
    height: 1200px;
    overflow: hidden;
    background: var(--white);
  }
  .dieline { display: block; width: 1200px; height: 1200px; }
  .panel-berry { fill: var(--berry); }
  .panel-pink { fill: var(--candy-pink); }
  .panel-mint { fill: var(--mint); }
  .brand-name {
    font-family: "Tinos", "Times New Roman", serif;
    font-weight: 700;
    fill: var(--white);
    text-anchor: middle;
  }
  .brand-name--small { font-size: 40px; }
  .brand-name--large { font-size: 72px; }
  .box-copy {
    font-family: "Tinos", "Times New Roman", serif;
    font-weight: 700;
    font-size: 9.6px;
    fill: var(--white);
    text-anchor: middle;
  }
</style>
</head>
<body>
<svg class="dieline" viewBox="0 0 1200 1200" xmlns="http://www.w3.org/2000/svg">
  <defs>
    <linearGradient id="confetti-band" x1="0" y1="0" x2="1" y2="0">
      <stop offset="0" stop-color="#c95ba9"/>
      <stop offset="0.3" stop-color="#f2a77a"/>
      <stop offset="0.55" stop-color="#7fb9d8"/>
      <stop offset="0.8" stop-color="#d37bb0"/>
      <stop offset="1" stop-color="#f0b277"/>
    </linearGradient>
    <radialGradient id="confetti-scatter-a" cx="0.2" cy="0.2" r="0.8">
      <stop offset="0" stop-color="#f1a372" stop-opacity="0.9"/>
      <stop offset="0.5" stop-color="#9c6cc0" stop-opacity="0.5"/>
      <stop offset="1" stop-color="#e66fa2" stop-opacity="0"/>
    </radialGradient>
    <radialGradient id="confetti-scatter-b" cx="0.8" cy="0.8" r="0.8">
      <stop offset="0" stop-color="#6fb4e0" stop-opacity="0.8"/>
      <stop offset="0.5" stop-color="#f2a77a" stop-opacity="0.45"/>
      <stop offset="1" stop-color="#e66fa2" stop-opacity="0"/>
    </radialGradient>
  </defs>

  <!-- back wall -->
  <path class="panel-berry" d="M288,200 L912,200 L912,296 L904,304 L296,304 L288,296 Z"/>

  <!-- side dust flaps -->
  <rect class="panel-mint" x="182" y="304" width="222" height="242"/>
  <rect class="panel-mint" x="796" y="304" width="222" height="244"/>

  <!-- base panel -->
  <rect class="panel-pink" x="404" y="304" width="392" height="242"/>
  <text class="brand-name brand-name--small" x="594" y="364">Tartwhirl</text>
  <g class="box-copy">
    <text x="593" y="392">Lorem ipsum dolor sit amet, consectetuer adipiscing elit, sed diam</text>
    <text x="593" y="405">nonummy nibh euismod tincidunt ut laoreet dolore magna aliquam</text>
    <text x="593" y="418">erat volutpat. veniam, quis nostrud exerci tation</text>
    <text x="593" y="432">ullamcorper suscipit lobortis nisl ut aliquip ex ea commodo consequat.</text>
    <text x="593" y="445">Duis autem vel eum iriure dolor in hendrerit in vulputate velit</text>
    <text x="593" y="458">esse molestie consequat, vel illum dolore eu feugiat nulla facilisis at vero</text>
    <text x="593" y="472">eros et accumsan et iusto odio dignissim qui blandit praesent luptatum</text>
    <text x="593" y="485">zzril augue duis dolore te feugait nulla facilisi.</text>
  </g>
  <rect x="404" y="498" width="392" height="48" fill="url(#confetti-band)" opacity="0.85"
        role="img" aria-label="Band of multicoloured confetti dots along the panel edge"/>

  <!-- front wall -->
  <path class="panel-berry" d="M296,546 L904,546 L912,552 L912,650 L288,650 L288,552 Z"/>

  <!-- lid side flaps -->
  <path class="panel-berry" d="M413,654 L352,670 Q308,682 308,720 L308,830 Q308,868 352,878 L413,894 Z"/>
  <path class="panel-berry" d="M788,654 L849,670 Q892,682 892,720 L892,830 Q892,868 849,878 L788,894 Z"/>

  <!-- lid top -->
  <rect class="panel-pink" x="413" y="652" width="375" height="242"/>
  <rect x="413" y="652" width="220" height="130" fill="url(#confetti-scatter-a)"
        role="img" aria-label="Scattered multicoloured confetti dots in the upper left corner"/>
  <rect x="600" y="800" width="188" height="94" fill="url(#confetti-scatter-b)"
        role="img" aria-label="Scattered multicoloured confetti dots in the lower right corner"/>
  <text class="brand-name brand-name--large" x="600" y="826">Tartwhirl</text>

  <!-- lid front tuck -->
  <path class="panel-berry" d="M304,902 L413,897 L788,897 L894,902 Q898,904 897,912 Q892,1000 808,1000 L392,1000 Q306,1000 303,912 Q302,904 304,902 Z"/>
</svg>
</body>
</html>
```